We need a brochure designed for a presentation to a new client based around the use of Horizontal Directional Drilling and the installation of culverts with its use. Not all photos are required to be used.
The process used to install culverts is as follows:1)Survey the site and grade changes2)Set up drill to required pitch3)Drill pilot bore4)Pre-ream to required diameter5)Assemble culverts and install pulling adapter6)Pull culvert back behind reamer7)Install requested aggregate material around culvert ends. Horizontal Directional Drilling is on average 30% less in cost compared to traditional open excavation methods and can generally be completed 40% faster. HDD can be used to install a large amount of different products. For example you can install corrugated(culverts), steel pipe, HDPE pipe, PVC pipe, and many more. The following industries have benefitted from the use of trenchless technology over the years: Oil & Gas, Power & Telecommunications, Highway & road Construction, Water and sewer. HDD provides a safer and more cost effective alternative to open cut methods by allowing traffic to flow without disruption and limit the time workers and crew members have to spend on road ways and trenches providing a safer work environment.

Target Market(s)

new clients and local highway improvement governments

Colors

Designer to choose colors to be used in the design.

Requirements
Must have
• Provide some pictures, description of how to do the installation, cost advantages with a graph or pie chart, and the safety factors
Nice to have
• Types of product that can be installed and industries that use the technology
• Or company colours are black, grey, and orange
Should not have
• no false information or misleading info

```html
<!DOCTYPE html>
<html lang="en">
<head>
<meta charset="utf-8">
<title>Horizontal Directional Drilling Brochure – Outside</title>
<link href="https://fonts.googleapis.com/css2?family=Montserrat:wght@400;500;600;700;800&display=swap" rel="stylesheet">
<style>
  :root {
    --orange: #ee5a24;
    --orange-deep: #d9471a;
    --orange-light: #f47a3c;
    --ink: #1e1e1e;
    --black: #1b1b1b;
    --grey: #8c8c8c;
    --pale: #e4e4e4;
    --white: #ffffff;
    --stage: #ececec;
  }
  * { box-sizing: border-box; margin: 0; padding: 0; }
  html, body { width: 1200px; height: 922px; overflow: hidden; }
  body { background: var(--stage); font-family: "Montserrat", sans-serif; color: var(--ink); }

  .brochure {
    position: absolute; left: 0; top: 38px;
    width: 1328px; height: 936px;
    transform: scale(0.9036); transform-origin: top left;
    background: var(--white); overflow: hidden;
  }

  .cover-photo {
    position: absolute; left: 663px; top: 0; width: 665px; height: 600px;
    background: linear-gradient(160deg, #f1f3f5 0%, #dfe3e6 35%, #b9bec2 60%, #6e6a63 85%, #4d473f 100%);
  }
  .shapes { position: absolute; inset: 0; }

  /* Inside-left text */
  .section-title { position: absolute; left: 35px; font-size: 20px; font-weight: 500; letter-spacing: .2px; }
  .section-title .accent { color: var(--orange); }
  .section-title strong { font-weight: 700; }
  .who-title { top: 30px; padding-left: 14px; border-left: 1.5px solid var(--orange); line-height: 18px; }
  .who-text {
    position: absolute; left: 35px; top: 56px; width: 588px;
    font-size: 15.4px; line-height: 20.7px; text-align: justify;
  }
  .process-title {
    top: 190px; padding-left: 14px; border-left: 1.5px solid var(--grey);
    font-size: 22px; line-height: 28px;
  }
  .process-title .accent { display: block; font-weight: 500; }
  .process-title strong { display: block; }
  .steps { position: absolute; left: 35px; top: 254px; list-style: none; }
  .steps li {
    display: flex; align-items: center; gap: 12px;
    font-size: 15.8px; line-height: 24.6px;
  }
  .steps svg { width: 14px; height: 14px; flex: none; }

  .photo-round {
    position: absolute; border-radius: 50%;
    border: 7px solid var(--white);
    box-shadow: 0 3px 10px rgba(0,0,0,.35);
  }
  .photo-bore { left: 28px; top: 517px; width: 222px; height: 222px;
    background: radial-gradient(circle at 45% 55%, #8b8478 0%, #6b6659 45%, #d9d6d0 100%); }
  .photo-pipe { left: 262px; top: 430px; width: 188px; height: 188px;
    background: linear-gradient(135deg, #dfe4ea 0%, #b8c0c7 45%, #e6eaee 70%, #c96a3c 100%); }
  .photo-adapter { left: 487px; top: 410px; width: 146px; height: 146px;
    background: radial-gradient(circle at 55% 45%, #3a3a3a 0%, #8d9195 40%, #d7dade 100%); }

  .contact { position: absolute; left: 205px; width: 264px; top: 680px; text-align: center; color: var(--white); }
  .contact h3 { font-size: 19px; font-weight: 400; }
  .contact h3 strong { font-weight: 700; }
  .contact .rule { display: block; width: 42px; height: 1.5px; background: var(--white); margin: 7px auto 14px; }
  .contact p { font-size: 18.5px; line-height: 33px; display: flex; align-items: center; justify-content: center; gap: 6px; }
  .contact svg { width: 16px; height: 16px; }

  .web-left { position: absolute; left: 22px; top: 880px; color: var(--white); }
  .web-left small { display: block; font-size: 11.5px; }
  .web-left strong { display: block; font-size: 27px; font-weight: 800; line-height: 30px; }

  /* Cover */
  .cover-title { position: absolute; left: 686px; top: 503px; }
  .cover-title h1 { font-size: 42px; font-weight: 700; line-height: 47px; color: var(--pale); }
  .cover-title h2 { font-size: 36px; font-weight: 400; line-height: 44px; color: var(--ink); letter-spacing: .6px; margin-top: 3px; }
  .cover-title .rule { display: block; width: 46px; height: 3px; background: var(--pale); margin-top: 13px; }
  .web-right { position: absolute; left: 686px; top: 900px; font-size: 14px; letter-spacing: 2.2px; color: #cfcfcf; }

  .brand { position: absolute; left: 1050px; top: 708px; width: 260px; text-align: center; }
  .brand-mark { display: block; width: 120px; height: 120px; border-radius: 50%; border: 7px solid var(--orange); margin: 0 auto 26px; }
  .brand-name { color: var(--orange); font-weight: 800; font-size: 30px; line-height: 30px; letter-spacing: 1px; }
  .brand-name span { display: block; font-size: 16.5px; line-height: 22px; letter-spacing: 1.4px; }
</style>
</head>
<body>
<div class="brochure">
  <div class="cover-photo" role="img" aria-label="Photo: worker in hi-vis gear walking beside a long corrugated steel culvert pulled through a snowy ditch"></div>

  <svg class="shapes" viewBox="0 0 1328 936" aria-hidden="true">
    <defs>
      <linearGradient id="orangeSweep" x1="0" y1="0" x2="1" y2="1">
        <stop offset="0" stop-color="#f47a3c"/>
        <stop offset=".5" stop-color="#ee5a24"/>
        <stop offset="1" stop-color="#d9471a"/>
      </linearGradient>
    </defs>
    <path d="M0,700 C150,610 420,520 663,478 C900,440 1150,420 1328,365 L1328,936 L0,936 Z" fill="url(#orangeSweep)"/>
    <path d="M663,478 C900,440 1130,430 1328,365" fill="none" stroke="#ffffff" stroke-width="4"/>
    <path d="M700,505 C950,480 1120,520 1200,548" fill="none" stroke="#ffffff" stroke-width="3" opacity=".85"/>
    <path d="M440,936 C720,850 1010,700 1328,455 L1328,936 Z" fill="var(--black)"/>
    <path d="M440,936 C720,850 1010,700 1328,455" fill="none" stroke="#ffffff" stroke-width="3"/>
    <path d="M560,936 C880,880 1150,770 1328,690" fill="none" stroke="var(--orange)" stroke-width="4"/>
    <path d="M0,832 C260,830 520,870 700,936" fill="none" stroke="#ffffff" stroke-width="7"/>
    <path d="M0,760 C60,715 140,660 220,610" fill="none" stroke="var(--black)" stroke-width="16"/>
    <path d="M230,580 C330,540 420,505 520,490" fill="none" stroke="var(--black)" stroke-width="10"/>
  </svg>

  <h2 class="section-title who-title"><span class="accent">WHO</span> <strong>WE ARE</strong></h2>
  <p class="who-text">Lorem Ipsum is simply dummy text of the printing and typesetting industry. Lorem Ipsum has been the industry's standard dummy text ever since the 1500s, when an unknown printer took a galley of type and scrambled it to make a type specimen book. It has survived not only five centuries, but also the leap into electronic typesetting, remaining essentially unchanged.</p>

  <h2 class="section-title process-title"><span class="accent">THE PROCESS USED TO INSTALL CULVERTS</span><strong>IS AS FOLLOWS :</strong></h2>
  <ul class="steps">
    <li><svg viewBox="0 0 14 14"><circle cx="7" cy="7" r="7" fill="var(--orange)"/><path d="M5.5,4 L8.5,7 L5.5,10" fill="none" stroke="#fff" stroke-width="1.8"/></svg>Survey the site and grade changes</li>
    <li><svg viewBox="0 0 14 14"><circle cx="7" cy="7" r="7" fill="var(--orange)"/><path d="M5.5,4 L8.5,7 L5.5,10" fill="none" stroke="#fff" stroke-width="1.8"/></svg>Set up drill to required pitch</li>
    <li><svg viewBox="0 0 14 14"><circle cx="7" cy="7" r="7" fill="var(--orange)"/><path d="M5.5,4 L8.5,7 L5.5,10" fill="none" stroke="#fff" stroke-width="1.8"/></svg>Drill pilot bore</li>
    <li><svg viewBox="0 0 14 14"><circle cx="7" cy="7" r="7" fill="var(--orange)"/><path d="M5.5,4 L8.5,7 L5.5,10" fill="none" stroke="#fff" stroke-width="1.8"/></svg>Pre-ream to required diameter</li>
    <li><svg viewBox="0 0 14 14"><circle cx="7" cy="7" r="7" fill="var(--orange)"/><path d="M5.5,4 L8.5,7 L5.5,10" fill="none" stroke="#fff" stroke-width="1.8"/></svg>Assemble culverts and install pulling adapter</li>
    <li><svg viewBox="0 0 14 14"><circle cx="7" cy="7" r="7" fill="var(--orange)"/><path d="M5.5,4 L8.5,7 L5.5,10" fill="none" stroke="#fff" stroke-width="1.8"/></svg>Pull culvert back behind reamer</li>
    <li><svg viewBox="0 0 14 14"><circle cx="7" cy="7" r="7" fill="var(--orange)"/><path d="M5.5,4 L8.5,7 L5.5,10" fill="none" stroke="#fff" stroke-width="1.8"/></svg>Install requested aggregate material around culvert ends.</li>
  </ul>

  <div class="photo-round photo-bore" role="img" aria-label="Photo: drill rod emerging from a rocky bore pit"></div>
  <div class="photo-round photo-pipe" role="img" aria-label="Photo: corrugated culvert with orange pulling cap lying on snow"></div>
  <div class="photo-round photo-adapter" role="img" aria-label="Photo: pulling adapter attached to the culvert end"></div>

  <div class="contact">
    <h3>Get <strong>in Touch</strong></h3>
    <span class="rule"></span>
    <p><svg viewBox="0 0 16 16"><path d="M8,15 C8,15 3,9.5 3,6 A5,5 0 0 1 13,6 C13,9.5 8,15 8,15 Z" fill="none" stroke="#fff" stroke-width="1.3"/><circle cx="8" cy="6" r="1.8" fill="none" stroke="#fff" stroke-width="1.3"/></svg>Address Goes Here</p>
    <p><svg viewBox="0 0 16 16"><path d="M3,2 L6,2 L7,5.5 L5.3,6.8 C6.2,8.8 7.4,10 9.3,10.8 L10.6,9.2 L14,10.2 L14,13.2 C8,13.8 2.4,8.2 3,2 Z" fill="none" stroke="#fff" stroke-width="1.2"/></svg>+0123 456 789</p>
    <p><svg viewBox="0 0 16 16"><rect x="1.5" y="3.5" width="13" height="9" fill="none" stroke="#fff" stroke-width="1.2"/><path d="M1.5,3.5 L8,9 L14.5,3.5" fill="none" stroke="#fff" stroke-width="1.2"/></svg>info@yourmailid.com</p>
  </div>

  <div class="web-left">
    <small>For More Information Visit Us at :</small>
    <strong>www.yourwebsite.com</strong>
  </div>

  <div class="cover-title">
    <h1>Horizontal<br>Directional Drilling</h1>
    <h2>and the Installation<br>of Culverts</h2>
    <span class="rule"></span>
  </div>

  <div class="web-right">www.yourwebsite.com</div>

  <div class="brand">
    <span class="brand-mark"></span>
    <p class="brand-name">BORELINE<span>CONTRACTING INC</span></p>
  </div>
</div>
</body>
</html>
```